Valtor Holidays Revamp Project 2015

We are a inbound Travel and tour operator based in Kuala Lumpur, Malaysia, established since 2010. Need a vibrant, dynamic, interactive and user friendly, we expect a Content management system for self data upload.
We cater to different markets around the world form Gulf, to the Far East.
Europe to Africa. With the minimum budget we give maximum services.
The final design should communicate well with the user and portray our growth.

Here is the reference of what our current website looks like.
www.valtorholidays-example.com.my

Target Market(s)

Far-East, South East Asia, Gulf market.

Industry/Entity Type

Travel

Number of Pages Required

5+ page

Font styles to use
Serif
Sans Serif
Other font styles liked:
• Calibri

Requirements
Must have
• User interaction, User friendly, Payment integration, should have a fun interface.
Should not have
• Should not have a complicated and overcrowded or jumbled up layout.

```html
<!DOCTYPE html>
<html lang="en">
<head>
<meta charset="utf-8">
<title>Valtor Holidays</title>
<link href="https://fonts.googleapis.com/css2?family=Open+Sans:ital,wght@0,300;0,400;0,600;0,700;1,400&display=swap" rel="stylesheet">
<style>
:root{
  --red:#cf1f2e;
  --ink:#2a2a2a;
  --muted:#6b6b6b;
  --white:#ffffff;
  --footer:#1f1f1f;
  --footer-deep:#141414;
  --line:#dcdcdc;
}
*{box-sizing:border-box;margin:0;padding:0}
html,body{width:1200px;height:4091px;overflow:hidden}
body{font-family:"Open Sans",Arial,sans-serif;color:var(--ink);background:var(--white);position:relative}
.section{position:absolute;left:0;width:1200px}
.title{font-weight:700;font-size:24px;text-align:center;letter-spacing:.5px;text-transform:uppercase}
.subtitle{font-size:14px;text-align:center;color:var(--muted)}

/* header */
.site-header{top:0;height:76px;background:var(--white);border-bottom:1px solid #eee}
.brand{position:absolute;left:95px;top:22px;display:flex;align-items:center;gap:10px;font-weight:700;font-size:22px;color:var(--red)}
.brand-dot{width:26px;height:26px;border-radius:50%;background:var(--red)}
.main-nav{position:absolute;left:578px;top:30px;display:flex;gap:0}
.main-nav a{font-size:12px;color:#555;text-decoration:none;text-transform:uppercase;width:87px;text-align:center}
.search-btn{position:absolute;left:1068px;top:22px;width:32px;height:32px;border-radius:50%;background:#eee}

/* hero */
.hero{top:76px;height:579px;background:linear-gradient(180deg,#b7b0a6 0%,#8d8279 45%,#5a4c43 75%,#3a2c26 100%)}
.hero-headline{position:absolute;left:518px;top:96px;color:var(--white)}
.hero-headline h1{font-size:25px;font-weight:700;letter-spacing:.5px}
.hero-headline p{font-size:25px;font-weight:300;letter-spacing:.5px;margin-top:2px}
.hero-arrow{position:absolute;top:254px;width:32px;height:32px;border-radius:50%;background:rgba(255,255,255,.25)}
.search-box{position:absolute;left:101px;top:450px;width:998px;height:96px;background:var(--white);padding:14px 18px}
.field{position:absolute;top:14px}
.field label{display:block;font-size:10px;font-weight:600;color:#444;text-transform:uppercase}
.field .input{margin-top:8px;height:34px;border:1px solid var(--line);font-size:11px;color:#999;padding:9px 10px}
.search-submit{position:absolute;left:842px;top:40px;width:140px;height:34px;background:var(--red);color:var(--white);font-weight:700;font-size:12px;text-align:center;line-height:34px}

/* welcome */
.welcome{top:655px;height:253px}
.welcome .title{margin-top:76px}
.welcome p{font-size:12px;color:var(--muted);text-align:center;line-height:26px;margin-top:22px}

/* why */
.why{top:908px;height:532px;background:linear-gradient(180deg,#2f5a64 0%,#1e4a54 50%,#163a40 100%)}
.why .title{color:var(--white);margin-top:62px}
.why-card{position:absolute;top:196px;width:298px;height:260px;background:var(--white);text-align:center;padding:90px 26px 0}
.why-icon{position:absolute;left:50%;top:-62px;margin-left:-62px;width:124px;height:124px;border-radius:50%;background:var(--white);display:flex;align-items:center;justify-content:center}
.why-icon span{width:104px;height:104px;border-radius:50%;background:var(--red);display:flex;align-items:center;justify-content:center}
.why-card h3{font-size:13px;font-weight:700;text-transform:uppercase}
.why-card p{font-size:11px;color:var(--muted);line-height:22px;margin-top:12px}

/* offers */
.offers{top:1440px;height:968px}
.offers .title{margin-top:78px}
.offers .subtitle{margin-top:8px;font-size:13px}
.offer-grid{position:absolute;top:193px;left:0;width:1200px;display:grid;grid-template-columns:repeat(3,1fr);grid-template-rows:repeat(3,257px);gap:2px}
.offer{position:relative;color:var(--white)}
.offer-caption{position:absolute;left:22px;right:22px;bottom:14px;display:flex;justify-content:space-between;align-items:flex-end}
.offer-caption .left,.offer-caption .right{display:flex;flex-direction:column}
.offer-caption .right{text-align:right}
.offer .loc{font-size:11px;font-weight:600;line-height:16px}
.offer .name{font-size:14px;font-weight:700;text-transform:uppercase;line-height:18px}
.offer .days{font-size:12px;font-weight:700;line-height:16px}
.offer .price{font-size:19px;font-weight:700;line-height:22px}

/* experience */
.experience{top:2408px;height:431px}
.experience .title{margin-top:80px}
.experience p.lead{width:1040px;margin:22px auto 0;font-size:12px;color:var(--muted);line-height:26px;text-align:center}
.experience blockquote{position:relative;width:760px;margin:40px auto 0;font-style:italic;font-size:15px;color:#777;text-align:center;line-height:30px}
.experience blockquote::before,.experience blockquote::after{position:absolute;font-size:40px;color:#bbb;font-style:normal}
.experience blockquote::before{content:"\201C";left:-40px;top:-10px}
.experience blockquote::after{content:"\201D";right:-40px;bottom:-30px}

/* news */
.news{top:2839px;height:524px;background:linear-gradient(180deg,#5b3b45 0%,#4a3a3f 50%,#2b2426 100%)}
.news .title{color:var(--white);margin-top:70px}
.news .subtitle{color:#e8e0e0;margin-top:4px}
.news-item{position:absolute;top:177px;width:308px;text-align:center;color:var(--white)}
.news-thumb{height:216px}
.news-item h4{font-size:13px;font-weight:700;text-transform:uppercase;margin-top:20px}
.news-item time{display:block;font-size:10px;margin-top:8px;color:#ddd}

/* testimonial */
.testimonial{top:3363px;height:368px}
.testimonial .title{margin-top:80px}
.avatar{position:absolute;left:232px;top:146px;width:120px;height:120px;border-radius:50%;background:linear-gradient(135deg,#e9dccf,#b99b83)}
.quote{position:absolute;left:423px;top:160px;width:530px;font-style:italic;font-size:15px;color:#777;line-height:28px}
.person{position:absolute;left:423px;top:246px}
.person strong{display:block;font-size:11px;color:var(--red);text-transform:uppercase;font-weight:700}
.person span{font-size:11px;color:var(--muted)}

/* footer */
.site-footer{top:3731px;height:305px;background:var(--footer);color:#cfcfcf}
.f-col{position:absolute;top:50px}
.f-col h5{font-size:13px;font-weight:700;color:var(--white);text-transform:uppercase;margin-bottom:14px}
.f-col li{list-style:none;font-size:11px;line-height:23.5px}
.contact li{display:flex;gap:10px;align-items:flex-start;line-height:20px;margin-bottom:8px}
.contact svg{flex:none;margin-top:3px}
.social li{display:flex;align-items:center;gap:10px;margin-bottom:14px}
.social .sq{width:22px;height:22px;background:var(--white)}
.badges{position:absolute;left:851px;top:182px;display:flex;gap:22px}
.badges span{width:80px;height:56px;border-radius:6px;background:#3a3a3a}
.bottom-bar{top:4036px;height:55px;background:var(--footer-deep);color:#bbb;font-size:11px;text-align:center;line-height:55px}
</style>
</head>
<body>

<header class="section site-header">
  <div class="brand"><span class="brand-dot"></span>Valtor Holidays</div>
  <nav class="main-nav">
    <a>Home</a><a>Tours</a><a>About Us</a><a>Pay Bills</a><a>Contact Us</a>
  </nav>
  <div class="search-btn"></div>
</header>

<section class="section hero" role="img" aria-label="Kuala Lumpur skyline with twin towers and city buildings">
  <div class="hero-headline">
    <h1>BRINGING GROUP TRAVEL TO A HIGHER STANDARD</h1>
    <p>TRAVELING WITH THE PROFESSIONALS!</p>
  </div>
  <div class="hero-arrow" style="left:26px"></div>
  <div class="hero-arrow" style="right:26px"></div>
  <form class="search-box">
    <div class="field" style="left:18px;width:240px"><label>Destination</label><div class="input">City, Region or keywords</div></div>
    <div class="field" style="left:270px;width:146px"><label>Date</label><div class="input">Departure</div></div>
    <div class="field" style="left:424px;width:146px"><label>&nbsp;</label><div class="input">Arrival</div></div>
    <div class="field" style="left:588px;width:240px"><label>Max Budgets</label><div class="input">USD 0 - 100</div></div>
    <div class="search-submit">SEARCH</div>
  </form>
</section>

<section class="section welcome">
  <h2 class="title">Welcome to Valtor Holidays</h2>
  <p>Malaysia is a country blessed with beautiful natural beaches and islands, as she is made up of a large peninsular and the third largest island in the world.<br>
  As Malaysia has a long history of civilisation and colonialisation, you can find traces of Portuguese, Dutch, English and Japanese architectural and cultural heritage in Malaysia.</p>
</section>

<section class="section why" role="img" aria-label="Mosque on the water at dusk">
  <h2 class="title">Why Choose Us</h2>
  <div class="why-card" style="left:104px">
    <div class="why-icon"><span><svg width="46" height="46" viewBox="0 0 46 46"><circle cx="23" cy="23" r="14" fill="none" stroke="#fff" stroke-width="4"/><circle cx="23" cy="23" r="5" fill="#fff"/></svg></span></div>
    <h3>Our Aim</h3>
    <p>Help our trade partners sell better than their competitors and our travel clients with a sizable trip. We strive to provide that delicate balance between competitive pricing, quality products and personalized customer service.</p>
  </div>
  <div class="why-card" style="left:451px">
    <div class="why-icon"><span><svg width="50" height="40" viewBox="0 0 50 40"><path d="M4 20 L16 10 L26 14 L34 10 L46 20 L30 32 L20 32 Z" fill="#fff"/></svg></span></div>
    <h3>Pricing &amp; Quality Service</h3>
    <p>Help our trade partners sell better than their competitors and our travel clients with a sizable trip. We strive to provide that delicate balance between competitive pricing, quality products and personalized customer service.</p>
  </div>
  <div class="why-card" style="left:797px">
    <div class="why-icon"><span><svg width="46" height="46" viewBox="0 0 46 46"><circle cx="23" cy="23" r="17" fill="#fff"/><path d="M12 18 Q20 14 22 22 Q26 28 20 34 M28 10 Q32 18 38 20" fill="none" stroke="#cf1f2e" stroke-width="3"/></svg></span></div>
    <h3>Tour Fleet</h3>
    <p>Help our trade partners sell better than their competitors and our travel clients with a sizable trip. We strive to provide that delicate balance between competitive pricing, quality products and personalized customer service.</p>
  </div>
</section>

<section class="section offers">
  <h2 class="title">Best Offers</h2>
  <p class="subtitle">Check out our best promotion tours</p>
  <div class="offer-grid">
    <article class="offer" role="img" aria-label="Kuala Lumpur twin towers at sunset" style="background:linear-gradient(180deg,#9aa6b8,#5a4a40)"><div class="offer-caption"><div class="left"><span class="loc">MALAYSIA</span><span class="name">Kuala Lumpur 3 Nights &amp;<br>Langkawi 2 Nights</span></div><div class="right"><span class="days">4 DAYS</span><span class="price">MYR705</span></div></div></article>
    <article class="offer" role="img" aria-label="Mosque on the waterfront at dusk" style="background:linear-gradient(180deg,#4f6fa8,#3a3a4a)"><div class="offer-caption"><div class="left"><span class="loc">MALAYSIA</span><span class="name">Kuala Lumpur 5 Days</span></div><div class="right"><span class="days">5 DAYS</span><span class="price">MYR825</span></div></div></article>
    <article class="offer" role="img" aria-label="Tropical island jetty over turquoise sea" style="background:linear-gradient(180deg,#2f6fb0,#2a9a9a)"><div class="offer-caption"><div class="left"><span class="loc">MALAYSIA</span><span class="name">Kuala Lumpur 7 Days</span></div><div class="right"><span class="days">4 DAYS</span><span class="price">MYR1,200</span></div></div></article>
    <article class="offer" role="img" aria-label="Beach with trees and umbrellas" style="background:linear-gradient(180deg,#7aa9c9,#8a8a6a)"><div class="offer-caption"><div class="left"><span class="loc">MALAYSIA</span><span class="name">Kuala Lumpur 10 Days</span></div><div class="right"><span class="days">10 DAYS</span><span class="price">MYR1,460</span></div></div></article>
    <article class="offer" role="img" aria-label="Resort huts over a lagoon" style="background:linear-gradient(180deg,#3a5a4a,#1a7a7a)"><div class="offer-caption"><div class="left"><span class="loc">MALAYSIA</span><span class="name">Demo 1</span></div><div class="right"><span class="days">7 DAYS</span><span class="price">MYR4,000</span></div></div></article>
    <article class="offer" role="img" aria-label="City towers lit at night" style="background:linear-gradient(180deg,#2a3a6a,#3a2a3a)"><div class="offer-caption"><div class="left"><span class="loc">MALAYSIA</span><span class="name">Demo 2</span></div><div class="right"><span class="days">30 DAYS</span><span class="price">MYR4,000</span></div></div></article>
    <article class="offer" role="img" aria-label="Green islands in a calm sea" style="background:linear-gradient(180deg,#3f7fc0,#1a4a5a)"><div class="offer-caption"><div class="left"><span class="loc">MALAYSIA</span><span class="name">Demo 3</span></div><div class="right"><span class="days">2 DAYS</span><span class="price">MYR8,000</span></div></div></article>
    <article class="offer" role="img" aria-label="Hillside village with mountains" style="background:linear-gradient(180deg,#6a8aa8,#3a4a30)"><div class="offer-caption"><div class="left"><span class="loc">MALAYSIA</span><span class="name">Kuala Lumpur 3 Days</span></div><div class="right"><span class="days">30 DAYS</span><span class="price">MYR345</span></div></div></article>
    <article class="offer" role="img" aria-label="Palm trees on a tropical beach" style="background:linear-gradient(180deg,#6aa8d8,#4a6a4a)"><div class="offer-caption"><div class="left"><span class="loc">MALAYSIA</span><span class="name">Kuala Lumpur 3 Days</span></div><div class="right"><span class="days">30 DAYS</span><span class="price">MYR345</span></div></div></article>
  </div>
</section>

<section class="section experience">
  <h2 class="title">A World of Experience</h2>
  <p class="lead">For a once in a lifetime experience, take an Valtor Holidays tour and discover the wonders of Malaysia – one of Asia's top holiday destinations. From pristine rainforests to silvery sand beaches and from sleek cityscapes to the rural wilds, this beautiful country brings together all the ingredients for a perfect holiday. All this, along with its friendly people and exciting cultures. It's hardly surprising that Malaysia has it all. As there is an incredible amount to see and do, we've picked out the best excursions so you don't miss the highlights.</p>
  <blockquote>Beautiful beaches, world- class infrastructure, mangroves rich in flora and fauna, ultra- cheap duty-free shopping and fascinating legends.</blockquote>
</section>

<section class="section news" role="img" aria-label="Water villas on a lagoon at sunset">
  <h2 class="title">News &amp; Update</h2>
  <p class="subtitle">Our latest news &amp; promotions</p>
  <article class="news-item" style="left:98px"><div class="news-thumb" role="img" aria-label="Snorkelling over a coral reef" style="background:linear-gradient(180deg,#2ab0c0,#1a7a8a)"></div><h4>Pulau Payar Marine Park Langkawi</h4><time>ON MAY 28, 2014</time></article>
  <article class="news-item" style="left:446px"><div class="news-thumb" role="img" aria-label="Island beach with boulders" style="background:linear-gradient(180deg,#4aa0e0,#d8d0b8)"></div><h4>Tioman Island</h4><time>ON MAY 28, 2014</time></article>
  <article class="news-item" style="left:792px"><div class="news-thumb" role="img" aria-label="Boats on a riverbank near a park" style="background:linear-gradient(180deg,#7aa8c8,#3a5a3a)"></div><h4>Kinabalu Park</h4><time>ON MAY 28, 2014</time></article>
</section>

<section class="section testimonial">
  <h2 class="title">What Customers Say</h2>
  <div class="avatar" role="img" aria-label="Customer portrait"></div>
  <p class="quote">Thinking of activities such as rich nature and cultural heritage, beach relaxing, snorkeling, river cruise...in Malaysia there is something for all families.</p>
  <div class="person"><strong>Maya Tan</strong><span>Marketing Executive</span></div>
</section>

<footer class="section site-footer">
  <div class="f-col" style="left:98px">
    <h5>Famous</h5>
    <ul><li>Batu Ferringhi Beach</li><li>Beady</li><li>Fun Kinabalu Park</li><li>Landscape</li><li>Langkawi</li><li>Nature</li><li>Pulau Payar Marine Park</li><li>Tioman Island</li></ul>
  </div>
  <div class="f-col" style="left:346px">
    <h5>Welcome</h5>
    <ul><li>Home</li><li>Tours</li><li>About Us</li><li>Pay Bills</li><li>Contact Us</li></ul>
  </div>
  <div class="f-col contact" style="left:543px;width:240px">
    <h5>Contact Us</h5>
    <ul>
      <li>Suite 5-2, 5th Floor Menara Lumira No.14 Jalan Seri Cahaya Kuala Lumpur Malaysia.</li>
      <li><svg width="12" height="12" viewBox="0 0 12 12"><path d="M2 1h3l1 3-2 1a7 7 0 0 0 3 3l1-2 3 1v3c-6 0-9-3-9-9z" fill="#fff"/></svg>00-60312345670</li>
      <li><svg width="12" height="12" viewBox="0 0 12 12"><path d="M2 1h3l1 3-2 1a7 7 0 0 0 3 3l1-2 3 1v3c-6 0-9-3-9-9z" fill="#fff"/></svg>00-60312345671</li>
      <li><svg width="12" height="12" viewBox="0 0 12 12"><rect x="1" y="2" width="10" height="8" fill="#fff"/><path d="M1 2l5 4 5-4" fill="none" stroke="#1f1f1f"/></svg>tours@valtorholidays-example.com.my</li>
      <li><svg width="12" height="12" viewBox="0 0 12 12"><circle cx="6" cy="6" r="5" fill="none" stroke="#fff" stroke-width="1.5"/></svg>www.valtorholidays-example.com.my</li>
    </ul>
  </div>
  <div class="f-col social" style="left:851px">
    <h5>Follow Us</h5>
    <ul><li><span class="sq"></span>/ Circlebook</li><li><span class="sq"></span>/ Chirper</li></ul>
  </div>
  <div class="badges"><span></span><span></span></div>
</footer>

<div class="section bottom-bar">Copyright © 2015, Valtor Holidays Sdn Bhd. &nbsp;/&nbsp; Terms &amp; Conditions &nbsp;/&nbsp; Privacy Policy</div>

</body>
</html>
```